sydney wedding photography business needs a business card design

we need a business card design for a sydney based wedding photography and videography business. our business name is :golden hour photography and video. our target clients are 24-35 yrs female. our style is candid, organic, natural, dynamic. we are a team of young photographers and videographers, and help brides to create memories that they will cherish for the rest of their lives. the logo will be provided. we want an elegant design that reflects our style, and also want to give a great impression to our clients that we are one of the best studios in sydney and our brand means quality and premium service.

Target Market(s)

bride to be, 24-35 years old, living in sydney and surrunding areas

Industry/Entity Type

Wedding Photography

Contact Information for Business Card

address: 57 marrow lane, bexton nsw 2041
mobile: 0431872056
phone: (02) 9361 2748
info@goldenhourstudio.net.au
www.goldenhourstudio.net.au
facebook:goldenhourbridals
instagram:goldenhourbridals

Font styles to use
Serif
Sans Serif

Requirements
Nice to have
• maybe add my slogan"memories beyond eternity" if the layout looks good
Should not have
• no black color, not good idea for wedding biz card

```html
<!DOCTYPE html>
<html lang="en">
<head>
<meta charset="utf-8">
<title>Golden Hour Photography and Video – Business Card</title>
<link rel="stylesheet" href="https://fonts.googleapis.com/css2?family=Didact+Gothic&display=swap">
<style>
  :root {
    --backdrop: #e9e6e2;
    --card-white: #ffffff;
    --blush: #ecdfef;
    --gold: #c9971c;
    --ink-soft: #8c8790;
    --ink-strong: #5e5862;
  }
  * { margin: 0; padding: 0; box-sizing: border-box; }
  html, body {
    width: 1200px;
    height: 799px;
    overflow: hidden;
    background: var(--backdrop);
    font-family: "Didact Gothic", sans-serif;
  }
  .canvas {
    position: relative;
    width: 1200px;
    height: 799px;
  }
  .card {
    position: absolute;
    top: 283px;
    width: 444px;
    height: 249px;
    background: var(--card-white);
    box-shadow: 0 2px 6px rgba(60, 50, 40, 0.18);
    overflow: hidden;
  }
  .card--front { left: 139px; }
  .card--back { left: 624px; }

  .front__band {
    position: absolute;
    top: 0; left: 0;
    width: 100%;
    height: 160px;
    background: var(--blush);
  }
  .wordmark {
    position: absolute;
    color: var(--gold);
    font-weight: 400;
    line-height: 1;
  }
  .wordmark__name {
    display: block;
    font-size: 30px;
    letter-spacing: 0.5px;
  }
  .wordmark__sub {
    display: block;
    margin-top: 6px;
    font-size: 10px;
    letter-spacing: 4px;
    padding-left: 30px;
  }
  .card--front .wordmark { left: 24px; top: 176px; }
  .card--back .wordmark { left: 24px; top: 16px; }

  .back__panel {
    position: absolute;
    top: 71px; left: 0;
    width: 100%;
    height: 178px;
    background: var(--blush);
    padding: 27px 0 0 23px;
  }
  .address {
    font-size: 8.5px;
    line-height: 12px;
    color: var(--ink-strong);
    font-weight: 400;
    margin-bottom: 20px;
  }
  .contact {
    list-style: none;
    font-size: 8px;
    line-height: 11.8px;
    color: var(--ink-soft);
  }
</style>
</head>
<body>
<main class="canvas">
  <section class="card card--front" aria-label="Business card front">
    <div class="front__band"></div>
    <div class="wordmark">
      <span class="wordmark__name">golden hour</span>
      <span class="wordmark__sub">PHOTOGRAPHY AND VIDEO</span>
    </div>
  </section>

  <section class="card card--back" aria-label="Business card back">
    <div class="wordmark">
      <span class="wordmark__name">golden hour</span>
      <span class="wordmark__sub">PHOTOGRAPHY AND VIDEO</span>
    </div>
    <div class="back__panel">
      <p class="address">57 marrow lane, bexton nsw<br>2041</p>
      <ul class="contact">
        <li>mobile: 0431872056</li>
        <li>phone: (02) 9361 2748</li>
        <li>info@goldenhourstudio.net.au</li>
        <li>www.goldenhourstudio.net.au</li>
        <li>facebook:goldenhourbridals</li>
        <li>instagram:goldenhourbridals</li>
      </ul>
    </div>
  </section>
</main>
</body>
</html>
```